Business Card Design

Mobile dog grooming

Industry/Entity Type

Business

Contact Information for Business Card

Bluefern Mobile Grooming
Marisol Teague
555-314-9072
www.bluefernmobilegrooming.example

```html
<!DOCTYPE html>
<html lang="en">
<head>
<meta charset="utf-8">
<title>Bluefern Mobile Grooming – Business Card</title>
<link href="https://fonts.googleapis.com/css2?family=Open+Sans:wght@400;600;700&display=swap" rel="stylesheet">
<style>
  :root {
    --purple-deep: #5a3d9e;
    --purple-mid: #7456b3;
    --purple-soft: #9a82cb;
    --art-light: #e6e9f6;
    --art-tone: #c9d3ee;
    --card-white: #ffffff;
    --backdrop: #ece9f1;
    --ink-white: #ffffff;
  }
  html, body {
    margin: 0;
    padding: 0;
    width: 1200px;
    height: 1000px;
    overflow: hidden;
    background: var(--backdrop);
    font-family: "Open Sans", Arial, sans-serif;
  }
  .canvas {
    position: relative;
    width: 1200px;
    height: 1000px;
  }
  .business-card {
    position: absolute;
    left: 75px;
    top: 200px;
    width: 1050px;
    height: 600px;
    background: var(--card-white);
    overflow: hidden;
    box-shadow: 0 10px 30px rgba(60, 40, 110, 0.18);
  }
  .wave {
    position: absolute;
    inset: 0;
    width: 1050px;
    height: 600px;
  }
  .wave-light { fill: var(--purple-soft); }
  .wave-mid { fill: var(--purple-mid); opacity: 0.85; }
  .wave-deep { fill: var(--purple-deep); }

  .mascot-art {
    position: absolute;
    left: 40px;
    top: 60px;
    width: 330px;
    height: 320px;
    border-radius: 24px;
    background: radial-gradient(circle at 50% 45%, var(--art-tone), var(--art-light) 70%, var(--card-white));
  }
  .company-name {
    position: absolute;
    left: 420px;
    top: 58px;
    margin: 0;
    font-size: 30px;
    font-weight: 700;
    color: var(--purple-deep);
  }
  .person-name {
    position: absolute;
    left: 420px;
    top: 140px;
    margin: 0;
    font-size: 56px;
    font-weight: 700;
    color: var(--purple-deep);
  }
  .contact {
    position: absolute;
    display: flex;
    align-items: center;
    gap: 16px;
    color: var(--ink-white);
    font-weight: 400;
    white-space: nowrap;
  }
  .contact-phone { left: 50px; top: 520px; font-size: 26px; }
  .contact-web { right: 40px; top: 505px; font-size: 24px; }
  .contact-icon {
    width: 38px;
    height: 38px;
    border-radius: 50%;
    background: var(--ink-white);
    display: flex;
    align-items: center;
    justify-content: center;
  }
  .contact-icon svg { width: 22px; height: 22px; fill: var(--purple-deep); }
</style>
</head>
<body>
<main class="canvas">
  <section class="business-card" aria-label="Bluefern Mobile Grooming business card">
    <svg class="wave" viewBox="0 0 1050 600" aria-hidden="true">
      <path class="wave-light" d="M0,600 L0,470 C220,470 360,250 600,270 C800,290 900,330 1050,320 L1050,600 Z"/>
      <path class="wave-mid" d="M0,600 L0,520 C260,520 420,360 660,380 C860,396 950,420 1050,410 L1050,600 Z"/>
      <path class="wave-deep" d="M0,600 L0,575 C300,570 480,450 720,460 C900,468 980,480 1050,475 L1050,600 Z"/>
    </svg>

    <div class="mascot-art" role="img" aria-label="Illustration of dogs in a grooming tub with soap bubbles"></div>

    <p class="company-name">Bluefern Mobile Grooming</p>
    <h1 class="person-name">Marisol Teague</h1>

    <div class="contact contact-phone">
      <span class="contact-icon">
        <svg viewBox="0 0 24 24" aria-hidden="true"><path d="M6.6 10.8a15.1 15.1 0 0 0 6.6 6.6l2.2-2.2a1 1 0 0 1 1-.25 11.4 11.4 0 0 0 3.6.57 1 1 0 0 1 1 1V20a1 1 0 0 1-1 1A17 17 0 0 1 3 4a1 1 0 0 1 1-1h3.5a1 1 0 0 1 1 1c0 1.25.2 2.45.57 3.57a1 1 0 0 1-.25 1z"/></svg>
      </span>
      <span class="contact-text">555-314-9072</span>
    </div>

    <div class="contact contact-web">
      <span class="contact-icon">
        <svg viewBox="0 0 24 24" aria-hidden="true"><path d="M12 3 2 12h3v8h5v-5h4v5h5v-8h3z"/></svg>
      </span>
      <span class="contact-text">www.bluefernmobilegrooming.example</span>
    </div>
  </section>
</main>
</body>
</html>
```